Online Psychiatry business - Business Card

I need a business card design. The target audience is busy professionals of any field (this therapy appeals best to 24-35 year olds). It involves psychiatry by tele-medicine (or video-conference). Nothing on it should be a giveaway that it's about mental health. Professional design with silver or gold as the primary colors appeals to me. The card must be as simple and as uncluttered as possible. Some color and flowing design on the edge of the card appeals to me.
CrestMindLink.com should probably appear in the center of the card and stand out, i.e. bold lettering, and easy to read, no cursive, but Ariel Black. Some where below this, should appear "Too Busy to Take Care of Yourself? Think again." Since this isn't office based, I don't think an office address is necessary and limits clutter.
Information that does need to appear is my name: Gerald Whitcombe, MD
General phone number: 541-876-2209. I'm hoping to get an 24-hour answering service soon so leave a little room for this. In addition I want to include two email addresses:
CrestMindLink@maildrop-box.com and CrestMind247@maildrop-box.com
Updates

I like the designs. I would like someone to put the website in bold in the center

 as most have been doing with a smaller font reminder nearby saying "No time" etc.
but I'd like to put my name down in the corner with the rest of the contact material.
Black print against a white or grey background appeals to me, with darker silver artwork near the sides (simple abstract, like wavy lines or something you can one up with that works. 
thanks

I ve tried to provide as much feedback as possible given my time limits, so if you have extra questions, please feel free to email. I tried to attach a file of a business card I really like but make be difficult to actually manufacture. I'm going to send you a link to the photo. The card has a pull tab. There is not much information on the outside. In fact, if you were to design the outside, I would just print : Too Busy to Take Care of Yourself? Think Again.

When you pull the tab the remaining information is on the bottom half of the card. Please don't use the color pink!!!!
http://www.layoutgallerypost.com/2009/05/100-clever-card-ideas/
It is the 39th photo on the list, about 2/3ds of the way down the page. It is titled: Faltenkästli

#7 and #16 have an appeal to me, except for the dot patterns
Hope this helps

I'm running out of time and energy. I 've been trying to give do down the list and give  individual feedback but I won't be able to do that anymore.

So if you have any specific questions, write me, and again thank you for all your effort!!

I know i received your files, including your zip files, Plonix,

but Gideon, did you send me the files including ZIP on project 5914386?
thanks

Target Market(s)

Working professionals and executive, attorneys, etc.

Industry/Entity Type

Business

Logo Text

Don't Have Time to Take Care of Yourself? Think Again.

Logo styles of interest
Pictorial/Combination Logo
Wordmark Logo
Other font styles liked:
• Ariel Black appeals to me the most

Requirements
Must have
• Want to emphasize that the website must be obvious, easily found (The CrestMindLink.com)
For that reason i'd like the card to be white, and minimal decoration on one or both sides just to add some style and color
Nice to have
• A Very uncluttered, elegant design, and something that makes it stick in your head-doesn't everyone want the last?
Should not have
• Nothing on the card that give it away that this is about psychiatry, such as brain or other symbol, but also nothing that gives it away as a medical business, such as a stethoscope or red cross or anything.

```html
<!DOCTYPE html>
<html lang="en">
<head>
<meta charset="utf-8">
<title>CrestMindLink.com – Business Card</title>
<link rel="stylesheet" href="https://fonts.googleapis.com/css2?family=Inter+Tight:wght@700;900&display=swap">
<style>
  :root {
    --brand-red: #bd2026;
    --paper: #ffffff;
    --fade-mid: #d9866f;
    --fade-light: #f3e2da;
    --tile-accent: #d66e5c;
    --type-display: "Inter Tight", "Arial Black", sans-serif;
    --type-body: "Inter Tight", Arial, sans-serif;
  }
  html, body {
    margin: 0;
    padding: 0;
    width: 900px;
    height: 1200px;
    overflow: hidden;
    background: var(--paper);
  }
  .card-sheet {
    position: relative;
    width: 900px;
    height: 1200px;
    background: var(--paper);
  }
  .card-face {
    position: absolute;
    left: 0;
    width: 900px;
    background: var(--brand-red);
  }
  .card-front { top: 0; height: 525px; }
  .card-back { top: 675px; height: 525px; }
  .card-face svg { display: block; position: absolute; inset: 0; }
  .site-name { font-family: var(--type-display); font-weight: 900; fill: var(--paper); }
  .holder-name { font-family: var(--type-body); font-weight: 700; fill: var(--brand-red); }
  .contact-line { font-family: var(--type-body); font-weight: 700; fill: var(--paper); }
  .tagline-lead, .tagline-punch { font-family: var(--type-display); font-weight: 900; fill: var(--paper); }
</style>
</head>
<body>
<main class="card-sheet">

  <section class="card-face card-front" aria-label="Card front with contact details">
    <svg width="900" height="525" viewBox="0 0 900 525" xmlns="http://www.w3.org/2000/svg">
      <defs>
        <linearGradient id="edgeFade" x1="270" y1="0" x2="900" y2="525" gradientUnits="userSpaceOnUse">
          <stop offset="0" stop-color="#bd2026"/>
          <stop offset="0.3" stop-color="#c53a30"/>
          <stop offset="0.55" stop-color="#d9866f"/>
          <stop offset="0.75" stop-color="#f3e2da"/>
          <stop offset="1" stop-color="#ffffff"/>
        </linearGradient>
      </defs>
      <rect class="edge-artwork" x="270" y="0" width="630" height="525" fill="url(#edgeFade)"
            role="img" aria-label="Abstract decorative fade from red into white along the right edge"/>

      <text class="site-name" x="30" y="240" font-size="34" textLength="495" lengthAdjust="spacingAndGlyphs">CRESTMINDLINK.COM</text>

      <g class="name-bar">
        <rect x="30" y="271" width="315" height="26" fill="var(--paper)"/>
        <rect x="345" y="271" width="27" height="26" fill="var(--tile-accent)"/>
        <text class="holder-name" x="37" y="290" font-size="15.5" letter-spacing="-0.4">GERALD WHITCOMBE, MD</text>
      </g>

      <g class="contact-block">
        <text class="contact-line" x="30" y="320" font-size="15" letter-spacing="-0.6">541-876-2209</text>
        <text class="contact-line" x="30" y="337" font-size="15" letter-spacing="-0.6">CRESTMINDLINK@MAILDROP-BOX.COM</text>
        <text class="contact-line" x="30" y="354" font-size="15" letter-spacing="-0.6">CRESTMIND247@MAILDROP-BOX.COM</text>
      </g>
    </svg>
  </section>

  <section class="card-face card-back" aria-label="Card back with tagline">
    <svg width="900" height="525" viewBox="0 0 900 525" xmlns="http://www.w3.org/2000/svg">
      <text class="tagline-lead" x="105" y="219" font-size="31" textLength="687" lengthAdjust="spacingAndGlyphs">NO TIME TO TAKE CARE OF YOURSELF?</text>
      <text class="tagline-punch" x="105" y="303" font-size="102" textLength="687" lengthAdjust="spacingAndGlyphs">THINK AGAIN.</text>
    </svg>
  </section>

</main>
</body>
</html>
```